Landingpage design for Movarabroker website

We need a design for a responsive 1 page landing page.
Good example: https://www.kelvaro.com/
On the homepage we will like to have a explanation video
attached you can find the logo's

About the website Movara.offers:
Movara.offers is a “Broker” we bring buyers and sellers together and facilitate transactions

Simple
quickly
Actuel
Compare (who is the best provider, at what price)
great offer
independent
1 invoice

Target Market(s)

BtoB

Number of Pages Required

1 page

Requirements
Must have
• On the homepage we will like to have a explanation video
Nice to have
• something between shipper and carrier and bring them togheter
• We will focus us first on fish transport... maybe you can add something
• Map from europe that shows our workarea

```html
<!DOCTYPE html>
<html lang="en">
<head>
<meta charset="utf-8">
<title>Movara Offers – Landing Page</title>
<link rel="stylesheet" href="https://fonts.googleapis.com/css2?family=Raleway:wght@500;600;700&family=Open+Sans:wght@400;600;700&display=swap">
<style>
:root{
  --blue:#2ba4d6;
  --blue-dark:#1f8fbf;
  --ink:#2a2a2a;
  --text:#444;
  --muted:#f3f3f3;
  --footer-bar:#1d1d1d;
  --white:#fff;
}
*{box-sizing:border-box;margin:0;padding:0}
html,body{width:1200px;height:4225px;overflow:hidden}
body{position:relative;background:var(--white);font-family:"Open Sans",Arial,sans-serif;color:var(--text)}
h2,h3{font-family:"Raleway",Arial,sans-serif;color:var(--ink)}
p{font-size:16px;line-height:21px}

/* header */
.site-header{position:absolute;top:0;left:0;width:1200px;height:124px;background:var(--white)}
.brand{position:absolute;left:0;top:0;width:310px;height:124px;background:var(--blue);display:flex;align-items:center;gap:16px;padding-left:40px}
.brand-dot{width:48px;height:48px;border-radius:50%;background:var(--white)}
.brand-name{font-family:"Raleway",sans-serif;font-weight:700;font-size:28px;line-height:30px;color:var(--white)}
.account-links{position:absolute;top:8px;left:868px;display:flex;gap:25px}
.account-links a{display:block;height:26px;line-height:26px;text-align:center;font-size:15px;color:var(--white);text-decoration:none;border-radius:3px}
.btn-login{width:124px;background:var(--blue)}
.btn-register{width:133px;background:var(--footer-bar)}
.main-nav{position:absolute;top:52px;left:482px;display:flex;font-family:"Raleway",sans-serif;font-size:15px;font-weight:600}
.main-nav a{color:var(--blue);text-decoration:none;margin-right:50px;letter-spacing:.5px}
.main-nav a.active{color:var(--ink);border-bottom:3px solid var(--ink);padding-bottom:8px}
.nav-icons{position:absolute;top:50px;left:1052px;display:flex;gap:44px}

/* hero */
.hero{position:absolute;top:124px;left:0;width:1200px;height:575px;background:linear-gradient(180deg,#d9dde2 0%,#c4cbd2 55%,#e6e8ea 100%)}
.hero-trucks{position:absolute;left:150px;top:30px;width:900px;height:420px;background:linear-gradient(90deg,#e2521c 0%,#f07a18 50%,#f2b514 100%);opacity:.85;border-radius:6px}
.hero-cta{position:absolute;top:462px;height:45px;background:#3b3b3b;border-radius:23px;color:var(--white);font-family:"Raleway",sans-serif;font-weight:600;font-size:17px;letter-spacing:.5px;display:flex;align-items:center;justify-content:center}
.hero-cta .tick{position:absolute;left:-12px;top:-12px}
.hero-dots{position:absolute;top:538px;left:546px;display:flex;gap:10px}
.hero-dots span{width:15px;height:15px;border-radius:50%;background:#9dcbe3}
.hero-dots span:first-child{background:var(--blue)}

/* intro */
.intro{position:absolute;top:699px;left:0;width:1200px;height:484px;background:var(--muted)}
.intro-copy{position:absolute;left:76px;top:112px;width:340px}
.intro-copy .lead{font-family:"Raleway",sans-serif;font-weight:700;font-size:16px;line-height:22px;color:var(--ink);margin-bottom:20px}
.intro-copy p{margin-bottom:20px}
.btn{display:flex;align-items:center;justify-content:space-between;height:40px;padding:0 14px 0 20px;background:var(--blue);color:var(--white);font-size:14px;font-style:italic;font-weight:600;text-decoration:none;position:absolute}
.video{position:absolute;left:575px;top:48px;width:557px;height:394px;background:var(--white);box-shadow:0 4px 10px rgba(0,0,0,.25);padding:8px}
.video-frame{width:100%;height:335px;background:linear-gradient(160deg,#6b7f95 0%,#41505f 50%,#9aa5ae 100%)}
.video-bar{height:30px;margin-top:6px;background:#d8d8d8;display:flex;align-items:center;gap:12px;padding:0 10px}
.video-bar i{display:block;width:10px;height:10px;background:#555}
.video-bar .track{flex:1;height:4px;background:#999}

/* feature rows */
.feature{position:absolute;left:0;width:1200px;height:455px}
.feature-media{position:absolute;top:0;height:100%}
.feature-copy{position:absolute;top:40px;width:432px}
.feature-copy h2{font-size:20px;font-weight:700;margin-bottom:22px}
.feature-copy p{margin-bottom:20px}
.feature-copy .btn{position:relative;width:158px;font-style:normal;font-size:13px}

/* stats */
.stats{position:absolute;top:3178px;left:0;width:1200px;height:239px;background:linear-gradient(180deg,#39a8d6,#2f9fcf)}
.stat{position:absolute;top:44px;width:240px;text-align:center;color:var(--white)}
.stat-ring{width:124px;height:124px;margin:0 auto;border:3px solid var(--white);border-radius:50%;display:flex;align-items:center;justify-content:center;font-family:"Raleway",sans-serif;font-size:32px;font-weight:600}
.stat-label{margin-top:24px;font-size:15px;letter-spacing:.8px;font-weight:600}

/* contact */
.contact{position:absolute;top:3417px;left:0;width:1200px;height:358px}
.contact-map{position:absolute;left:99px;top:48px;width:481px;height:254px;background:linear-gradient(135deg,#e9e4d8,#cfe0c5 60%,#b8d3e6);box-shadow:0 2px 6px rgba(0,0,0,.2)}
.contact-copy{position:absolute;left:648px;top:56px;width:470px}
.contact-copy h2{font-size:22px;font-weight:600;margin-bottom:22px}
.contact-list{margin-top:24px;font-size:14px;line-height:18px;display:grid;grid-template-columns:70px 1fr}

/* footer */
.site-footer{position:absolute;top:3775px;left:0;width:1200px;height:380px;background:var(--blue);color:var(--white)}
.footer-brand{position:absolute;left:64px;top:60px;display:flex;align-items:center;gap:14px;font-family:"Raleway",sans-serif;font-weight:700;font-size:24px;line-height:26px}
.footer-brand .brand-dot{width:40px;height:40px}
.footer-col{position:absolute;width:220px}
.footer-col h3{color:var(--white);font-size:17px;font-weight:700;margin-bottom:6px;display:flex;align-items:center;gap:10px}
.footer-col p{font-size:13px;line-height:17px}
.footer-icon{position:absolute;width:72px;height:72px;border:3px solid var(--white);border-radius:50%;display:flex;align-items:center;justify-content:center}
.bottom-bar{position:absolute;top:4155px;left:0;width:1200px;height:70px;background:var(--footer-bar);color:var(--white);font-size:15px}
.bottom-bar .copy{position:absolute;left:100px;top:24px}
.socials{position:absolute;left:848px;top:18px;display:flex;gap:11px}
.socials span{width:34px;height:34px;border-radius:50%;background:var(--white)}
</style>
</head>
<body>

<header class="site-header">
  <div class="brand"><span class="brand-dot"></span><span class="brand-name">MOVARA<br>OFFERS</span></div>
  <div class="account-links"><a class="btn-login" href="#">Login</a><a class="btn-register" href="#">Register</a></div>
  <nav class="main-nav">
    <a class="active" href="#">HOME</a><a href="#">ABOUT US</a><a href="#">PRICING</a><a href="#">FAQ</a><a href="#">CONTACT</a>
  </nav>
  <div class="nav-icons">
    <svg width="24" height="24" viewBox="0 0 24 24" fill="none" stroke="#2ba4d6" stroke-width="3"><circle cx="10" cy="10" r="7"/><line x1="15" y1="15" x2="22" y2="22"/></svg>
    <svg width="26" height="22" viewBox="0 0 26 22" stroke="#2ba4d6" stroke-width="3"><line x1="0" y1="3" x2="26" y2="3"/><line x1="0" y1="11" x2="26" y2="11"/><line x1="0" y1="19" x2="26" y2="19"/></svg>
  </div>
</header>

<section class="hero">
  <div class="hero-trucks" role="img" aria-label="Three heavy trucks in red, orange and yellow parked side by side"></div>
  <div class="hero-cta" style="left:234px;width:315px">GREAT OFFER
    <svg class="tick" width="68" height="68" viewBox="0 0 68 68"><circle cx="34" cy="34" r="31" fill="#6bb33a" stroke="#fff" stroke-width="4"/><path d="M18 35l11 11 22-24" fill="none" stroke="#fff" stroke-width="7"/></svg>
  </div>
  <div class="hero-cta" style="left:654px;width:318px">COMPARE
    <svg class="tick" width="68" height="68" viewBox="0 0 68 68"><circle cx="34" cy="34" r="31" fill="#6bb33a" stroke="#fff" stroke-width="4"/><path d="M18 35l11 11 22-24" fill="none" stroke="#fff" stroke-width="7"/></svg>
  </div>
  <div class="hero-dots"><span></span><span></span><span></span><span></span></div>
</section>

<section class="intro">
  <div class="intro-copy">
    <p class="lead">Looking For a Tranport Company ?<br>Looking For a Loading ?</p>
    <p>We Bring you together and find the bestand most efficient way for your shipment.</p>
    <p>You are a view steps away from the easiest way to organize your transports</p>
  </div>
  <a class="btn" href="#" style="left:76px;top:400px;width:217px">Get a Free Estimate
    <svg width="26" height="20" viewBox="0 0 26 20" fill="none" stroke="#fff" stroke-width="3"><line x1="0" y1="10" x2="23" y2="10"/><path d="M14 2l9 8-9 8"/></svg></a>
  <a class="btn" href="#" style="left:310px;top:400px;width:214px">Become a Carrier
    <svg width="26" height="20" viewBox="0 0 26 20" fill="none" stroke="#fff" stroke-width="3"><line x1="0" y1="10" x2="23" y2="10"/><path d="M14 2l9 8-9 8"/></svg></a>
  <div class="video">
    <div class="video-frame" role="img" aria-label="Explanation video still: a truck driving on a coastal road">
      <svg width="541" height="335" viewBox="0 0 541 335"><path d="M250 140v56l46-28z" fill="#fff"/></svg>
    </div>
    <div class="video-bar"><i></i><i></i><i></i><span class="track"></span><i></i></div>
  </div>
</section>

<section class="feature" style="top:1220px">
  <div class="feature-media" role="img" aria-label="Truck on a mountain highway under a cloudy sky" style="left:0;width:648px;background:linear-gradient(160deg,#b7c4cf 0%,#5d6b78 55%,#2c333a 100%);clip-path:polygon(0 0,540px 0,648px 100%,0 100%)"></div>
  <div class="feature-copy" style="left:679px">
    <h2>Why should i use movara offers?</h2>
    <p>Lorem Ipsum is simply dummy text of the printing and typesetting industry. Lorem Ipsum has been the industry's standard dummy text ever since the 1500s, when an unknown printer took a galley of type and a type specimen book.</p>
    <p>It has survived not only five centuries, but also the leap into electronic typesetting, remaining essentially unchanged. It was popularised in the 1960s with the like Velsor Pagesetter including versions of Lorem Ipsum.</p>
    <a class="btn" href="#">Read more <svg width="26" height="20" viewBox="0 0 26 20" fill="none" stroke="#fff" stroke-width="3"><line x1="0" y1="10" x2="23" y2="10"/><path d="M14 2l9 8-9 8"/></svg></a>
  </div>
</section>

<section class="feature" style="top:1713px">
  <div class="feature-copy" style="left:101px">
    <h2>Transport Solutions</h2>
    <p>Lorem Ipsum is simply dummy text of the printing and typesetting industry. Lorem Ipsum has been the industry's standard dummy text ever since the 1500s, when an unknown printer took a galley of type and a type specimen book.</p>
    <p>It has survived not only five centuries, but also the leap into electronic typesetting, remaining essentially unchanged. It was popularised in the 1960s with the like Velsor Pagesetter including versions of Lorem Ipsum.</p>
    <a class="btn" href="#">Read more <svg width="26" height="20" viewBox="0 0 26 20" fill="none" stroke="#fff" stroke-width="3"><line x1="0" y1="10" x2="23" y2="10"/><path d="M14 2l9 8-9 8"/></svg></a>
  </div>
  <div class="feature-media" role="img" aria-label="Stacked cardboard parcels on a pallet in a warehouse" style="left:552px;width:648px;background:linear-gradient(135deg,#d89a48 0%,#c07a2c 50%,#f0c060 100%);clip-path:polygon(108px 0,648px 0,648px 100%,0 100%)"></div>
</section>

<section class="feature" style="top:2203px">
  <div class="feature-media" role="img" aria-label="Map of Europe showing the work area" style="left:0;width:648px;background:linear-gradient(160deg,#a9cde8 0%,#e8e4d6 45%,#d9e5c6 100%);clip-path:polygon(0 0,560px 0,648px 100%,0 100%)"></div>
  <div class="feature-copy" style="left:679px">
    <h2>Destanition Europe</h2>
    <p>Lorem Ipsum is simply dummy text of the printing and typesetting industry. Lorem Ipsum has been the industry's standard dummy text ever since the 1500s, when an unknown printer took a galley of type and a type specimen book.</p>
    <p>It has survived not only five centuries, but also the leap into electronic typesetting, remaining essentially unchanged. It was popularised in the 1960s with the like Velsor Pagesetter including versions of Lorem Ipsum.</p>
    <a class="btn" href="#">Read more <svg width="26" height="20" viewBox="0 0 26 20" fill="none" stroke="#fff" stroke-width="3"><line x1="0" y1="10" x2="23" y2="10"/><path d="M14 2l9 8-9 8"/></svg></a>
  </div>
</section>

<section class="feature" style="top:2690px">
  <div class="feature-copy" style="left:101px">
    <h2>Free ?</h2>
    <p>Lorem Ipsum is simply dummy text of the printing and typesetting industry. Lorem Ipsum has been the industry's standard dummy text ever since the 1500s, when an unknown printer took a galley of type and a type specimen book.</p>
    <p>It has survived not only five centuries, but also the leap into electronic typesetting, remaining essentially unchanged. It was popularised in the 1960s with the like Velsor Pagesetter including versions of Lorem Ipsum.</p>
    <a class="btn" href="#">Read more <svg width="26" height="20" viewBox="0 0 26 20" fill="none" stroke="#fff" stroke-width="3"><line x1="0" y1="10" x2="23" y2="10"/><path d="M14 2l9 8-9 8"/></svg></a>
  </div>
  <div class="feature-media" role="img" aria-label="Black price tag reading free over a faded truck scene" style="left:552px;width:648px;background:linear-gradient(135deg,#f2f2f2 0%,#d6d6d6 55%,#bdbdbd 100%);clip-path:polygon(108px 0,648px 0,648px 100%,0 100%)"></div>
</section>

<section class="stats">
  <div class="stat" style="left:125px"><div class="stat-ring">3.5M</div><div class="stat-label">SHIPPING CUSTOMERS</div></div>
  <div class="stat" style="left:466px"><div class="stat-ring">9.5M</div><div class="stat-label">SERVICE PROVIDERS</div></div>
  <div class="stat" style="left:815px"><div class="stat-ring">8.5M</div><div class="stat-label">SHIPMENT LISTINGS</div></div>
</section>

<section class="contact">
  <div class="contact-map" role="img" aria-label="Street map with the office location"></div>
  <div class="contact-copy">
    <h2>Contact us</h2>
    <p>Lorem Ipsum is simply dummy text of the printing and typesetting industry.</p>
    <div class="contact-list">
      <span>Address :</span><span>48 Harbor Lane, Norvik, NV 20417</span>
      <span>Phone :</span><span>+ 31 20 555 0148</span>
      <span>Fax :</span><span>+ 31 20 555 0149</span>
      <span>Email :</span><span>info@movaraoffers.com</span>
      <span>Chat :</span><span>Movara Offers</span>
    </div>
  </div>
</section>

<footer class="site-footer">
  <div class="footer-brand"><span class="brand-dot"></span><span>MOVARA<br>OFFERS</span></div>
  <div class="footer-icon" style="left:414px;top:64px"><svg width="30" height="30" viewBox="0 0 30 30" fill="none" stroke="#fff" stroke-width="4"><path d="M25 15a10 10 0 1 1-3-7"/><path d="M23 2v7h-7"/></svg></div>
  <div class="footer-icon" style="left:670px;top:64px"><svg width="30" height="30" viewBox="0 0 30 30" fill="none" stroke="#fff" stroke-width="3"><rect x="3" y="5" width="24" height="20"/><line x1="8" y1="12" x2="22" y2="12"/><line x1="8" y1="18" x2="22" y2="18"/></svg></div>
  <div class="footer-icon" style="left:930px;top:64px"><svg width="30" height="30" viewBox="0 0 30 30" fill="none" stroke="#fff" stroke-width="3"><rect x="5" y="3" width="20" height="24"/><line x1="10" y1="10" x2="20" y2="10"/><line x1="10" y1="16" x2="20" y2="16"/><line x1="10" y1="22" x2="20" y2="22"/></svg></div>

  <div class="footer-col" style="left:104px;top:140px"><h3>Contact us</h3><p>Lorem Ipsum is simply dummy text of the printing and typesetting industry.</p></div>
  <div class="footer-col" style="left:420px;top:140px"><h3>Want more ?</h3><p>Lorem Ipsum is simply dummy text of the printing and typesetting industry.</p></div>
  <div class="footer-col" style="left:673px;top:140px"><h3>Press</h3><p>Lorem Ipsum is simply dummy text of the printing and typesetting industry.</p></div>
  <div class="footer-col" style="left:935px;top:140px"><h3>Blog</h3><p>Lorem Ipsum is simply dummy text of the printing and typesetting industry.</p></div>

  <div class="footer-col" style="left:104px;top:255px"><h3><svg width="20" height="20"><circle cx="10" cy="10" r="8" fill="none" stroke="#fff" stroke-width="2.5"/></svg>Services</h3><p>Lorem Ipsum is simply dummy text of the printing.</p></div>
  <div class="footer-col" style="left:420px;top:255px"><h3><svg width="20" height="20"><circle cx="10" cy="10" r="8" fill="none" stroke="#fff" stroke-width="2.5"/></svg>Foundation</h3><p>Lorem Ipsum is simply dummy text of the printing.</p></div>
  <div class="footer-col" style="left:673px;top:255px;width:250px"><h3><svg width="20" height="20"><circle cx="10" cy="10" r="8" fill="none" stroke="#fff" stroke-width="2.5"/></svg>Movara Offers Apps</h3><p>Lorem Ipsum is simply dummy text of the printing.</p></div>
  <div class="footer-col" style="left:935px;top:255px"><h3><svg width="20" height="20"><circle cx="10" cy="10" r="8" fill="none" stroke="#fff" stroke-width="2.5"/></svg>Expo</h3><p>Lorem Ipsum is simply dummy text of the printing.</p></div>
</footer>

<div class="bottom-bar">
  <span class="copy">© 2017 Movara Offers &nbsp;•&nbsp; Privacy Policy</span>
  <div class="socials"><span></span><span></span><span></span><span></span><span></span><span></span><span></span></div>
</div>

</body>
</html>
```